New Website for ReBranded Company - CrewBeacon

We have a successful company and website currently but it is a little dated. We have re-branded the company from Harbor Signal Networks to CrewBeacon and have a new logo for the new name. We are looking to build a newer fresher website with the new name. I will need a concept of the home page and one inside page. You can see our current site at https://www.harborsignalnetworks.example and the new site will be https://www.crewbeacon.example .

I also really like the https://www.pathlantern.example/ website. I like ledgerkite.example website. I like the https://skillorbit.example/ website.

See the attached document for layout and some text to use. Use the pictures I attached as opposed to pictures from the old site as much as you can.

Target Market(s)

Business

Industry/Entity Type

Software Service

Number of Pages Required

2 page

Font styles to use
Sans Serif

Requirements
Must have
• Use the colors from my logo. Professional but modern. We want people to feel like our product makes their staff feel safer at work.
Should not have
• Don't use any red or orange (no stop colors).

```html
<!DOCTYPE html>
<html lang="en">
<head>
<meta charset="utf-8">
<title>CrewBeacon – Home and Inner Page Concept</title>
<link href="https://fonts.googleapis.com/css2?family=Outfit:wght@400;500;600;700&display=swap" rel="stylesheet">
<style>
:root{
  --blue:#2f97d4;
  --blue-dark:#1f7fbf;
  --green:#7cc245;
  --ink:#2b2f33;
  --muted:#5d6670;
  --mist:#f1f2f4;
  --stage:#ffffff;
  --white:#ffffff;
}
*{box-sizing:border-box;margin:0;padding:0}
html,body{width:1110px;height:1200px;overflow:hidden;background:var(--stage);font-family:"Outfit",Arial,sans-serif;color:var(--ink)}
.page{position:absolute;background:var(--white);box-shadow:0 10px 40px rgba(0,0,0,.12);overflow:hidden}
.page--home{left:76px;top:45px;width:468px;height:1114px}
.page--inner{left:571px;top:45px;width:468px;height:642px;background:var(--mist)}
.abs{position:absolute}
/* header */
.site-header{position:absolute;left:0;top:0;width:100%;height:37px;background:var(--white)}
.page--inner .site-header{background:transparent}
.brand{position:absolute;left:51px;top:10px;display:flex;align-items:center;gap:4px;color:var(--blue);font-weight:500;font-size:9px}
.brand__dot{width:12px;height:12px;border-radius:50%;background:var(--blue)}
.nav{position:absolute;top:16px;left:138px;display:flex;gap:13px;font-size:4px;color:var(--blue);font-weight:500}
.btn{position:absolute;display:flex;align-items:center;justify-content:center;border-radius:8px;color:var(--white);font-size:4.3px;font-weight:600;box-shadow:0 1px 3px rgba(0,0,0,.2)}
.btn--blue{background:var(--blue)}
.btn--green{background:var(--green)}
.btn--square{border-radius:1px}
/* hero */
.hero{position:absolute;left:0;top:37px;width:468px;height:145px}
.hero__panel{position:absolute;left:0;top:0;width:274px;height:145px;background:var(--blue)}
.hero__photo{position:absolute;left:274px;top:0;width:194px;height:145px;background:linear-gradient(160deg,#3a3d42,#17191c)}
.hero__notch{position:absolute;left:273px;top:66px}
.hero__title{position:absolute;left:69px;top:36px;color:var(--white);font-size:14.5px;font-weight:500;line-height:17px}
.hero__title b{font-weight:700}
.hero__lede{position:absolute;left:68px;top:83px;color:var(--white);font-size:5.6px;font-weight:500}
/* feature card */
.feature-card{position:absolute;left:78px;top:173px;width:312px;height:77px;background:var(--white);box-shadow:0 2px 8px rgba(0,0,0,.18);border-radius:2px}
.feature{position:absolute;top:10px;width:100px;text-align:center;font-size:3.6px;line-height:5px;color:var(--ink)}
.feature svg{display:block;margin:0 auto 9px}
h2.section-title{position:absolute;left:0;width:100%;text-align:center;font-weight:600;color:var(--ink)}
.caps{text-transform:uppercase;letter-spacing:.3px}
.center-text{position:absolute;left:0;width:100%;text-align:center;font-size:6px;line-height:9px}
/* why */
.ill{position:absolute;border-radius:4px}
.why-col{position:absolute;top:446px;width:90px;text-align:center}
.why-col h3{font-size:6.4px;font-weight:600;color:var(--blue);line-height:7px}
.why-col p{font-size:3.8px;line-height:5.5px;color:var(--blue);margin-top:3px}
.opts{display:grid;grid-template-columns:1fr 1fr;text-align:left;width:58px;margin:0 auto;font-size:3.8px;line-height:5.5px;color:var(--blue)}
/* proof */
.proof__text{position:absolute;left:92px;top:563px;width:140px;font-size:6.4px;line-height:9px}
.proof__stat{position:absolute;left:92px;top:620px;font-size:10px;font-weight:700;color:var(--blue);white-space:nowrap}
.proof__stat small{font-size:6px;font-weight:500}
.photo{position:absolute;width:66px;height:50px}
/* plan */
.plan-box{position:absolute;top:722px;width:77px;height:68px;background:var(--white);box-shadow:0 1px 4px rgba(0,0,0,.15)}
.plan-box h4{height:18px;background:var(--blue);color:var(--white);font-size:4.6px;font-weight:600;display:flex;align-items:center;justify-content:center;text-align:center;line-height:5px;padding:0 4px}
.plan-box ul{list-style:none;padding:7px 0 0 8px;font-size:4.6px;line-height:9px;color:var(--blue)}
.plan-box ul li::before{content:"≡ ";font-size:3.5px}
.plan-box p{font-size:4.6px;line-height:5.6px;color:var(--blue);text-align:center;padding:7px 8px 0}
.plan-link{position:absolute;top:753px}
/* band */
.band{position:absolute;left:0;top:811px;width:468px;height:132px;background:var(--blue)}
.band h2{position:absolute;left:88px;top:27px;color:var(--white);font-size:11px;font-weight:600;line-height:14.5px}
/* footer */
.footer{position:absolute;left:0;width:468px;height:180px}
.footer__call{position:absolute;left:87px;top:0;color:var(--blue);font-size:11px;font-weight:700;line-height:14.5px;white-space:nowrap}
.footer__blurb{position:absolute;left:87px;top:32px;width:108px;font-size:5px;line-height:9px;color:var(--blue)}
.footer__brand{position:absolute;left:87px;top:88px;display:flex;align-items:center;gap:5px;color:var(--blue);font-size:13px;font-weight:500}
.footer__brand span.dot{width:19px;height:19px;border-radius:50%;background:var(--blue)}
.footer__col{position:absolute;top:15px;width:70px;text-align:center;color:var(--blue);font-size:4.8px;line-height:11.2px}
.footer__col h5{font-size:8px;font-weight:600;letter-spacing:.4px;margin-bottom:5px;line-height:10px}
.footer__copy{position:absolute;left:87px;top:125px;font-size:3.6px;color:var(--blue)}
/* inner */
.inner-title{position:absolute;left:0;top:68px;width:100%;text-align:center;color:var(--blue);font-size:12.5px;font-weight:600;letter-spacing:.3px}
.inner-copy{position:absolute;left:82px;top:133px;width:304px;text-align:center;font-size:5.5px;line-height:9px;color:var(--ink)}
.inner-copy p+p{margin-top:9px}
</style>
</head>
<body>

<!-- HOME PAGE -->
<section class="page page--home">
  <header class="site-header">
    <div class="brand"><span class="brand__dot"></span>CrewBeacon</div>
    <nav class="nav"><span>Home</span><span>Buy Addons</span><span>Cust Login</span></nav>
    <span class="btn btn--blue btn--square" style="left:361px;top:12px;width:59px;height:14px">Explore Your Choices →</span>
  </header>

  <div class="hero">
    <div class="hero__panel"></div>
    <div class="hero__photo" role="img" aria-label="Photo of a staff member wearing a panic button on a lanyard"></div>
    <svg class="hero__notch" width="12" height="16" viewBox="0 0 12 16"><path d="M0 0 L12 8 L0 16Z" fill="#2f97d4"/></svg>
    <h1 class="hero__title">Feel <b>Confident</b><br>That Your Staff Is Protected</h1>
    <p class="hero__lede">Get a revolutionary new electronic panic button</p>
    <span class="btn btn--green" style="left:69px;top:106px;width:62px;height:14px">Ready To Get Started</span>
  </div>

  <div class="feature-card">
    <div class="feature" style="left:4px">
      <svg width="40" height="40" viewBox="0 0 40 40" fill="none" stroke="#2f97d4" stroke-width="1.2"><rect x="2" y="6" width="32" height="32"/><path d="M18 6v32M2 22h32"/><circle cx="34" cy="6" r="5"/><path d="M31 6l2 2 4-4"/></svg>
      Problems Stopped Before They Start<br>For Any Type Of Organization
    </div>
    <div class="feature" style="left:106px">
      <svg width="48" height="40" viewBox="0 0 48 40" fill="none" stroke="#2f97d4" stroke-width="1.2"><rect x="2" y="4" width="44" height="34" rx="3"/><rect x="32" y="15" width="14" height="11" rx="2"/><text x="12" y="28" font-size="18" fill="#2f97d4" stroke="none" font-family="Outfit,Arial,sans-serif">$</text></svg>
      Affordable Prices Starting at $18 per month.<br>No Contracts. No Hidden Costs
    </div>
    <div class="feature" style="left:208px">
      <svg width="48" height="40" viewBox="0 0 48 40" fill="none" stroke="#2f97d4" stroke-width="1.2"><rect x="2" y="2" width="36" height="28" rx="2"/><path d="M14 38h14M20 30v8"/><rect x="34" y="14" width="12" height="22" rx="2" fill="#fff"/><path d="M20 8l-7 13h14z"/></svg>
      Alerts by computer, mobile device, text,phone,<br>email, monitoring and E911
    </div>
  </div>

  <h2 class="section-title caps" style="top:265px;font-size:11px;line-height:16px">Your Employees Shouldn’t Feel Alone<br>When They Need Help</h2>
  <p class="center-text" style="top:299px">Does this problem make you feel frustrated and anxious?<br>Put a simple solution in their hands</p>
  <span class="btn btn--blue" style="left:208px;top:324px;width:52px;height:12px">Ready To Get Started</span>

  <svg class="abs" style="left:0;top:340px" width="468" height="200" viewBox="0 0 468 200" preserveAspectRatio="none">
    <path d="M0 25 C90 0 160 -5 260 10 C350 22 420 15 468 0 V170 C400 185 330 195 250 175 C160 155 80 160 0 180Z" fill="#f1f2f4"/>
  </svg>

  <h2 class="section-title" style="top:363px;font-size:11px">Why Businesses Choose Us</h2>
  <div class="ill" style="left:102px;top:390px;width:72px;height:46px;background:linear-gradient(135deg,#cfe6f5,#9bcbe9)" role="img" aria-label="Illustration of a laptop with a chat window and alert button"></div>
  <div class="ill" style="left:207px;top:386px;width:52px;height:55px;background:radial-gradient(circle,#a8d77f 0 25%,#8fc4ea 26%,#d8ecf8 70%)" role="img" aria-label="Illustration of a person surrounded by communication channel icons"></div>
  <div class="ill" style="left:306px;top:390px;width:60px;height:50px;background:radial-gradient(circle at 50% 30%,#7cc245 0 30%,#cfe6f5 31%,#a9d3ef 80%)" role="img" aria-label="Illustration of two hands holding a dollar coin"></div>

  <div class="why-col" style="left:86px">
    <h3>Easy To Use</h3>
    <p>Press a button and let the right people know you need help and open a chat window letting everyone talk on resolving their problem</p>
  </div>
  <div class="why-col" style="left:188px">
    <h3>Communicate the Way<br>You Want</h3>
    <p>We give you lots of options:</p>
    <div class="opts"><span>Computer</span><span>Phone call</span><span>Mobile</span><span>Text</span><span>Email</span><span>E911</span><span></span><span>Call Center</span></div>
  </div>
  <div class="why-col" style="left:291px">
    <h3>Cost Effective<br>Protection</h3>
    <p>By leveraging your existing network and equipment we can lower your costs to give better options to your staff</p>
  </div>
  <span class="btn btn--blue" style="left:318px;top:500px;width:59px;height:14px">Ready To Get Started</span>

  <p class="proof__text">We know how scary it can feel to worry about employee safety.<br><br>That’s why we have provided a way for customers to get help to staff effectively in</p>
  <p class="proof__stat">45 States <small>covering</small> 5 Countries</p>
  <span class="btn btn--blue" style="left:92px;top:650px;width:59px;height:14px">Start My Demo</span>
  <div class="photo" style="left:240px;top:561px;background:linear-gradient(135deg,#7d8a93,#2f3438)" role="img" aria-label="Photo of a desk phone with panic button"></div>
  <div class="photo" style="left:310px;top:561px;background:linear-gradient(135deg,#c9b89b,#6e6253)" role="img" aria-label="Photo of several panic button devices on a table"></div>
  <div class="photo" style="left:240px;top:614px;background:linear-gradient(135deg,#3f4f6a,#141a24)" role="img" aria-label="Photo of a panic button carried in a pocket"></div>
  <div class="photo" style="left:310px;top:614px;background:linear-gradient(135deg,#9a9fa3,#43484c)" role="img" aria-label="Photo of a button mounted under a desk"></div>

  <svg class="abs" style="left:0;top:665px" width="468" height="146" viewBox="0 0 468 146" preserveAspectRatio="none">
    <path d="M0 45 C120 20 250 30 330 20 C400 12 440 5 468 0 V146 H0Z" fill="#f1f2f4"/>
  </svg>
  <h2 class="section-title" style="top:694px;font-size:11px">Simple Start Plan</h2>
  <div class="abs" style="left:214px;top:711px;width:40px;height:1.5px;background:var(--blue)"></div>

  <div class="plan-box" style="left:89px"><h4>Explore Your Choices</h4><ul><li>Pricing</li><li>Trial</li><li>Quote</li><li>Hardware</li></ul></div>
  <div class="plan-box" style="left:195px"><h4>Get Setup</h4><ul><li>Input Your Alerts</li><li>Input Your Staff</li><li>Install Our Software</li></ul></div>
  <div class="plan-box" style="left:301px"><h4>Feel Confident Your Staff Is Protected</h4><p>High Five. You just too a major step to getting rid of the anxiety and frustration this gave you</p></div>
  <svg class="plan-link" style="left:169px" width="24" height="8" viewBox="0 0 24 8"><path d="M0 4h24M20 1l3 3-3 3" stroke="#2f97d4" stroke-width=".8" fill="none"/><circle cx="11" cy="4" r="3.5" fill="#2f97d4"/><path d="M9.3 4l1.2 1.2 2-2" stroke="#fff" stroke-width=".7" fill="none"/></svg>
  <svg class="plan-link" style="left:275px" width="24" height="8" viewBox="0 0 24 8"><path d="M0 4h24M20 1l3 3-3 3" stroke="#2f97d4" stroke-width=".8" fill="none"/><circle cx="11" cy="4" r="3.5" fill="#2f97d4"/><path d="M9.3 4l1.2 1.2 2-2" stroke="#fff" stroke-width=".7" fill="none"/></svg>

  <div class="band">
    <h2>Stay Connected with Staff<br>during a Crisis Situations</h2>
    <span class="btn btn--green" style="left:92px;top:82px;width:59px;height:14px">Start My Demo</span>
    <div class="abs" style="left:222px;top:24px;width:178px;height:95px;border-radius:3px;background:linear-gradient(160deg,#f4f6f8,#c9d2da)" role="img" aria-label="Laptop and phone screens showing the alert dashboard"></div>
  </div>

  <footer class="footer" style="top:973px">
    <div class="footer__call">Call Us<br>1 – 800 – 555 – 0142</div>
    <p class="footer__blurb">When employees feel alone during a threatening situation, we give them a way to let the right resources know that they need help so you can feel confident that your staff is protected.</p>
    <div class="footer__brand"><span class="dot"></span>CrewBeacon</div>
    <div class="footer__col" style="left:211px"><h5>SHOP</h5>Add Ons<br>Start My Demo<br>Custom Quote<br>Start Trial</div>
    <div class="footer__col" style="left:276px"><h5>ABOUT</h5>Affiliates<br>Contact<br>Support<br>Existing Customers<br>Industries<br>Blog<br>FAQ</div>
    <div class="footer__col" style="left:339px"><h5>LEGAL</h5>Privacy Policy<br>Terms of Use<br>End User License<br><span style="display:block;margin-top:-6px">Agreement</span></div>
    <p class="footer__copy">©CrewBeacon 2020</p>
  </footer>
</section>

<!-- INNER PAGE -->
<section class="page page--inner">
  <svg class="abs" style="left:0;top:0" width="468" height="516" viewBox="0 0 468 516" preserveAspectRatio="none">
    <path d="M0 125 C90 110 180 85 280 100 C360 112 420 110 468 100 V455 C400 420 330 410 260 425 C170 445 80 420 0 430Z" fill="#fff"/>
    <rect x="0" y="472" width="468" height="170" fill="#fff"/>
  </svg>
  <header class="site-header">
    <div class="brand"><span class="brand__dot"></span>CrewBeacon</div>
    <nav class="nav"><span>Home</span><span>Buy Addons</span><span>Cust Login</span></nav>
    <span class="btn btn--blue btn--square" style="left:361px;top:14px;width:59px;height:14px">Explore Your Choices →</span>
  </header>

  <h1 class="inner-title">LOREM IPSUM DOLOR SIT AMET</h1>
  <div class="inner-copy">
    <p>Lorem ipsum dolor sit amet, consectetur adipiscing elit, sed do eiusmod tempor incididunt ut labore et dolore magna aliqua. Ultricies integer quis auctor elit sed. Libero nunc consequat interdum varius sit amet mattis vulputate. Neque sodales ut etiam sit amet nisl purus. Congue quisque egestas diam in arcu cursus euismod. Cursus mattis molestie a iaculis. Nunc sed augue lacus viverra vitae congue eu. At quis risus sed vulputate. Vitae congue eu consequat ac felis. Vulputate enim nulla aliquet porttitor lacus. Non enim praesent elementum facilisis leo vel. Ut consequat semper viverra nam libero justo laoreet sit amet. Lacus sed viverra tellus in hac habitasse. Commodo sed egestas egestas fringilla phasellus faucibus. Ut ornare lectus sit amet est placerat in. Aenean et tortor at risus viverra adipiscing at.</p>
    <p>Suspendisse faucibus interdum posuere lorem ipsum dolor sit. Vitae congue mauris rhoncus aenean vel elit scelerisque mauris pellentesque. Est sit amet facilisis magna etiam tempor orci eu lobortis. Interdum varius sit amet mattis. Fames ac turpis egestas integer eget aliquet. Vitae et leo duis ut diam quam. Facilisi nullam vehicula ipsum a arcu cursus vitae. Egestas pretium aenean pharetra magna ac placerat vestibulum lectus mauris. Consequat id porta nibh venenatis cras sed felis eget. Eget aliquet nibh praesent tristique magna sit amet purus. Suspendisse ultrices gravida dictum fusce ut placerat. Dictum fusce ut placerat orci nulla pellentesque. Non odio euismod lacinia at quis risus sed. Nec ullamcorper sit amet risus nullam eget felis eget. Amet justo donec enim diam. Duis tristique sollicitudin nibh sit amet. Lacus suspendisse faucibus interdum posuere. Id diam maecenas ultricies mi eget mauris. Tempus iaculis urna id volutpat lacus laoreet.</p>
  </div>

  <footer class="footer" style="top:496px">
    <div class="footer__call">Call Us<br>1 – 800 – 555 – 0142</div>
    <p class="footer__blurb">When employees feel alone during a threatening situation, we give them a way to let the right resources know that they need help so you can feel confident that your staff is protected.</p>
    <div class="footer__brand"><span class="dot"></span>CrewBeacon</div>
    <div class="footer__col" style="left:211px"><h5>SHOP</h5>Add Ons<br>Start My Demo<br>Custom Quote<br>Start Trial</div>
    <div class="footer__col" style="left:276px"><h5>ABOUT</h5>Affiliates<br>Contact<br>Support<br>Existing Customers<br>Industries<br>Blog<br>FAQ</div>
    <div class="footer__col" style="left:339px"><h5>LEGAL</h5>Privacy Policy<br>Terms of Use<br>End User License<br><span style="display:block;margin-top:-6px">Agreement</span></div>
    <p class="footer__copy">©CrewBeacon 2020</p>
  </footer>
</section>

</body>
</html>
```